IT’S NOT A CLEANING, IT’S YOUR LIFE! TOP TEN REASONS WHY THIS IS NOT JUST A “CLEANING”

We made a list for our patients to let them know why our hygiene appointments are different than other cleanings. Since this is a lot of information, we would like it easily readable within 4-5 feet but we do not want the post to be HUGE. Please see below:

IT’S NOT A CLEANING, IT’S YOUR LIFE!
TOP TEN REASONS WHY THIS IS NOT JUST A “CLEANING”

10. We make you look better. Healthy teeth and gums are more attractive. Recent studies
show that the smile is the first thing people notice and that people with better looking teeth
are more confident and successful.

9. We can relieve your headaches. During your hygiene visit we evaluate for serious bite
issues, many of which lead to muscle soreness, headaches, and migraines.

8. We check for oral cancer. Oral cancer kills 1 person per hour 24 hours a day. The death rate for oral cancer is higher than cancers we routinely hear about such as cervical, thyroid and skin cancer.

7. We make you smell better. During your hygiene visit we eliminate many of the germs that live under your gum tissue and cause bad breath.

6. We save you money. By utilizing the latest dental technology (digital x-rays, mouth
cameras, and magnification glasses) we can help with early detection of tooth and gum
problems and save you the cost of gum surgery, root canals, and implants.

5. We clean in places you cannot. We clean under the gum line and between teeth where
most of the germs hide and cause dental disease. 40% of the bacteria in your mouth lives in
between your teeth.

4. We prevent pain. We identify tooth decay that can lead to nerve involvement and pain,
root canal, and tooth loss.

3. We save your teeth. Most tooth loss is from periodontal/gum disease. At each visit we
evaluate the health of your gums and bone with our periodontal screening. Periodontal
disease, like high blood pressure, is symptomless until it is in advanced stages.

2. We protect your loved ones. Studies have proven that the bacteria that cause dental
disease can be transmitted from person to person. Think about that the next time you kiss
someone!

1. We prolong life. Researchers have linked the inflammation and infection found in the
mouth to heart attacks, strokes, and Alzheimer’s. By reducing infection in your mouth we can
greatly improve your overall health!

```html
<!DOCTYPE html>
<html lang="en">
<head>
<meta charset="utf-8">
<title>It's Not a Cleaning, It's Your Life!</title>
<link href="https://fonts.googleapis.com/css2?family=Oswald:wght@500;700&family=Roboto+Condensed:wght@700&display=swap" rel="stylesheet">
<style>
  :root {
    --sky: #1ba6e3;
    --white: #ffffff;
  }
  html, body {
    margin: 0;
    padding: 0;
    overflow: hidden;
    background: var(--sky);
  }
  .poster {
    position: relative;
    width: 861px;
    height: 1200px;
    background: var(--sky);
    color: var(--white);
    overflow: hidden;
  }
  .headline {
    position: absolute;
    top: 22px;
    left: 0;
    width: 100%;
    margin: 0;
    text-align: center;
    font-family: "Oswald", sans-serif;
    font-weight: 700;
    font-size: 92px;
    line-height: 96px;
    letter-spacing: 1px;
    text-transform: uppercase;
  }
  .headline span { display: block; }
  .subhead {
    position: absolute;
    top: 232px;
    left: 0;
    width: 100%;
    margin: 0;
    text-align: center;
    font-family: "Oswald", sans-serif;
    font-weight: 500;
    font-size: 35px;
    letter-spacing: 0.5px;
    text-transform: uppercase;
  }
  .rule {
    position: absolute;
    top: 300px;
    left: 44px;
    width: 773px;
    height: 3px;
    background: var(--white);
  }
  .spine {
    position: absolute;
    top: 303px;
    left: 429px;
    width: 3px;
    height: 897px;
    background: var(--white);
  }
  .reason {
    position: absolute;
    width: 330px;
    margin: 0;
    font-family: "Roboto Condensed", sans-serif;
    font-weight: 700;
    font-size: 14.5px;
    line-height: 19px;
    text-transform: uppercase;
    letter-spacing: 0.2px;
  }
  .reason.left { left: 46px; }
  .reason.right { left: 486px; }
  .badge {
    position: absolute;
    width: 36px;
    height: 40px;
    background: var(--white);
    color: var(--sky);
    font-family: "Oswald", sans-serif;
    font-weight: 700;
    font-size: 24px;
    line-height: 40px;
    text-align: center;
  }
  .badge.left { left: 388px; }
  .badge.right { left: 437px; }
</style>
</head>
<body>
<main class="poster">
  <h1 class="headline"><span>It's not a cleaning</span><span>It's your life!</span></h1>
  <p class="subhead">Top ten reasons why this is not just a “cleaning”</p>
  <div class="rule"></div>
  <div class="spine"></div>

  <p class="reason left" style="top:372px">We prolong life. Researchers have linked the inflammation and infection found in the mouth to heart attacks, strokes, and Alzheimer’s. By reducing infection in your mouth we can greatly improve your overall health!</p>
  <div class="badge left" style="top:390px">1</div>
  <div class="badge right" style="top:390px">6</div>
  <p class="reason right" style="top:372px">We save you money. By utilizing the latest dental technology (digital x-rays, mouth cameras, and magnification glasses) we can help with early detection of tooth and gum problems and save you the cost of gum surgery, root canals, and implants.</p>

  <p class="reason left" style="top:540px">We protect your loved ones. Studies have proven that the bacteria that cause dental disease can be transmitted from person to person. Think about that the next time you kiss someone!</p>
  <div class="badge left" style="top:556px">2</div>
  <div class="badge right" style="top:556px">7</div>
  <p class="reason right" style="top:540px">We make you smell better. During your hygiene visit we eliminate many of the germs that live under your gum tissue and cause bad breath.</p>

  <p class="reason left" style="top:700px">We save your teeth. Most tooth loss is from periodontal/gum disease. At each visit we evaluate the health of your gums and bone with our periodontal screening. Periodontal disease, like high blood pressure, is symptomless until it is in advanced stages.</p>
  <div class="badge left" style="top:728px">3</div>
  <div class="badge right" style="top:728px">8</div>
  <p class="reason right" style="top:700px">We check for oral cancer. Oral cancer kills 1 person per hour 24 hours a day. The death rate for oral cancer is higher than cancers we routinely hear about such as cervical, thyroid and skin cancer.</p>

  <p class="reason left" style="top:884px">We prevent pain. We identify tooth decay that can lead to nerve involvement and pain, root canal, and tooth loss.</p>
  <div class="badge left" style="top:894px">4</div>
  <div class="badge right" style="top:894px">9</div>
  <p class="reason right" style="top:868px">We make you look better. Healthy teeth and gums are more attractive. Recent studies show that the smile is the first thing people notice and that people with better looking teeth are more confident and successful.</p>

  <p class="reason left" style="top:1038px">We clean in places you cannot. We clean under the gum line and between teeth where most of the germs hide and cause dental disease. 40% of the bacteria in your mouth lives in between your teeth.</p>
  <div class="badge left" style="top:1056px">5</div>
  <div class="badge right" style="top:1056px">10</div>
  <p class="reason right" style="top:1038px">We can relieve your headaches. During your hygiene visit we evaluate for serious bite issues, many of which lead to muscle soreness, headaches, and migraines.</p>
</main>
</body>
</html>
```